Business Card for beauty technology startup

Design Glowmi Business Card for a Beauty, based on the website identity and colors (https://www.glowmi-example.com).
Glowmi is a beauty tech startup that gathers helpful product info for beauty lovers and consumers (such as availability on stores, price range and product reviews) for makeup products. The card design must be young, colorful but clean, and very modern.

Target Market(s)

woman, 15-35

Industry/Entity Type

Cosmetics

Contact Information for Business Card

Full Name, address, phone

Font styles to use
Other font styles liked:
• Advent Pro

Colors
e34297
86cfc6
ffffff
5c5c5c
e8e8e8
e667a6
b2b2b2

Requirements
Must have
• One full colored side with a creative design and another with card info
• Use Color palette: #95C5C5 and/or #D38AA5
• Use fonts: Advent Pro
• Use website identity: https://www.glowmi-example.com
Nice to have
• If needed extra font: Roboto

```html
<!DOCTYPE html>
<html lang="en">
<head>
<meta charset="utf-8">
<title>Glowmi Business Card</title>
<link rel="stylesheet" href="https://fonts.googleapis.com/css2?family=Roboto:wght@300;400;500&display=swap">
<style>
  :root {
    --backdrop: #e4e4e4;
    --card-light: #f4f4f4;
    --card-dark: #1a1b1e;
    --mauve: #b07d93;
    --mauve-deep: #6e4a5a;
    --ink: #4a4a4a;
    --ghost: #ece3e6;
    --white: #ffffff;
  }
  * { margin: 0; padding: 0; box-sizing: border-box; }
  html, body { width: 1200px; height: 960px; overflow: hidden; }
  body {
    position: relative;
    background: var(--backdrop);
    font-family: "Roboto", Arial, sans-serif;
  }
  .card {
    position: absolute;
    width: 600px;
    height: 343px;
    border-radius: 20px;
    overflow: hidden;
    box-shadow: 0 4px 8px rgba(0,0,0,0.35);
  }
  .card--front { left: 314px; top: 113px; background: var(--card-light); }
  .card--back  { left: 311px; top: 472px; background: var(--card-dark); }

  .front__ghost-circle {
    position: absolute;
    left: 10px; top: 90px;
    width: 240px; height: 240px;
    border-radius: 50%;
    border: 6px solid var(--ghost);
  }
  .front__name-band {
    position: absolute;
    left: 266px; top: 37px;
    width: 334px; height: 76px;
    background: var(--card-dark);
  }
  .front__title-band {
    position: absolute;
    left: 266px; top: 113px;
    width: 334px; height: 48px;
    background: var(--mauve-deep);
  }
  .front__badge {
    position: absolute;
    left: 214px; top: 36px;
    width: 126px; height: 126px;
    border-radius: 50%;
    background: var(--card-dark);
    border: 3px solid var(--mauve);
    display: flex; align-items: center; justify-content: center;
    color: var(--mauve);
    font-weight: 400;
    font-size: 24px;
  }
  .front__name {
    position: absolute;
    left: 354px; top: 68px;
    color: var(--mauve);
    font-weight: 500;
    font-size: 20px;
  }
  .front__role {
    position: absolute;
    left: 354px; top: 129px;
    color: var(--white);
    font-weight: 400;
    font-size: 15px;
  }
  .front__address {
    position: absolute;
    left: 355px; top: 184px;
    color: var(--ink);
    font-size: 14px;
    line-height: 18px;
  }
  .front__contacts {
    position: absolute;
    left: 355px; top: 231px;
    list-style: none;
    color: var(--ink);
    font-size: 14px;
    line-height: 19.3px;
  }
  .front__contacts li { display: flex; align-items: center; gap: 9px; }
  .front__contacts svg { width: 13px; height: 13px; fill: var(--mauve); flex: none; }

  .back__mark {
    position: absolute;
    left: 249px; top: 80px;
    width: 104px; height: 104px;
    border-radius: 50%;
    border: 3px solid var(--mauve);
  }
  .back__wordmark {
    position: absolute;
    left: 0; right: 0; top: 208px;
    text-align: center;
    color: var(--mauve);
    font-weight: 300;
    font-size: 42px;
    letter-spacing: 7px;
  }
  .back__web {
    position: absolute;
    left: 0; right: 0; top: 294px;
    text-align: center;
    color: var(--white);
    font-size: 14px;
    letter-spacing: 4px;
  }
</style>
</head>
<body>
  <section class="card card--front">
    <div class="front__ghost-circle"></div>
    <div class="front__name-band"></div>
    <div class="front__title-band"></div>
    <div class="front__badge">Glowmi</div>
    <h1 class="front__name">MAYA LUND</h1>
    <p class="front__role">CEO/FOUNDER</p>
    <address class="front__address">1420 Elm Court<br>Juneau, Alaska 34512</address>
    <ul class="front__contacts">
      <li><svg viewBox="0 0 16 16"><path d="M3.5 1l3 3-1.5 2c1 2 2.5 3.5 4.5 4.5l2-1.5 3 3-2 2C7 13 3 9 1.5 3z"/></svg>555 310 4821</li>
      <li><svg viewBox="0 0 16 16"><path d="M4 0h8v16H4zM5.5 2v10h5V2zM7 13.5h2v1H7z" fill-rule="evenodd"/></svg>555 718 2094</li>
      <li><svg viewBox="0 0 16 16"><path d="M4 1h8v4H4zM1 6h14v7h-3v2H4v-2H1zM5 10v4h6v-4z" fill-rule="evenodd"/></svg>555 264 7730</li>
      <li><svg viewBox="0 0 16 16"><path d="M1 3h14v10H1zM2 4l6 5 6-5z" fill-rule="evenodd"/></svg>info@glowmi-example.com</li>
      <li><svg viewBox="0 0 16 16"><circle cx="8" cy="8" r="7"/></svg>www.glowmi-example.com</li>
    </ul>
  </section>

  <section class="card card--back">
    <div class="back__mark"></div>
    <p class="back__wordmark">GLOWMI</p>
    <p class="back__web">www.glowmi-example.com</p>
  </section>
</body>
</html>
```